Media Training Presentation (template)

This is a 49-slide power point deck to be used in training clients to deal with the media in various settings. We need a template we can personalize for different clients. The overall color scheme should match our logo. It should look very professional, but also engaging. The word doc contains all of the text, images, and videos for each slide. Also uploaded our logo. Please match/coordinate colors of presentation to the logo colors. If you prefer, you can submit five or six slides showing the overall design and a template for each type of slide, then complete the remainder of the slides within 24 hours if chosen. (Sorry for the quick turnaround…we didn’t know we would need it this quickly!) Thanks for submitting!
Target Market(s)
Government and corporate clients

```html
<!DOCTYPE html>
<html lang="en">
<head>
<meta charset="utf-8">
<title>Media Training Presentation Template</title>
<link rel="stylesheet" href="https://fonts.googleapis.com/css2?family=Montserrat:wght@400;500;600;700&display=swap">
<style>
  :root{
    --stage:#58585a;
    --blue:#1356aa;
    --band-grey:#808080;
    --panel-grey:#d1d3d4;
    --title-grey:#7d7d7d;
    --white:#ffffff;
    --photo-dark:#4a4f4c;
  }
  *{box-sizing:border-box;margin:0;padding:0}
  html,body{width:1200px;height:960px;overflow:hidden;background:var(--stage)}
  body{position:relative;font-family:'Montserrat',Arial,sans-serif}
  .slide{position:absolute;width:348px;height:197px;background:var(--white);overflow:hidden}
  .col1{left:56px}.col2{left:422px}.col3{left:788px}
  .row1{top:57px}.row2{top:273px}.row3{top:488px}.row4{top:703px}

  /* section header band */
  .section-band{position:absolute;top:16px;left:0;height:19px;width:244px;display:flex;font-size:9.5px;font-weight:600;color:var(--white)}
  .section-band .num{background:var(--blue);width:73px;display:flex;align-items:center;justify-content:flex-end;padding-right:4px}
  .section-band .name{background:var(--band-grey);flex:1;display:flex;align-items:center;padding-left:4px}
  .brand{position:absolute;top:16px;left:252px;display:flex;align-items:center;gap:10px;color:var(--blue);font-weight:500}
  .brand .mark{width:13px;height:13px;border:1.6px solid var(--blue)}
  .brand .words{display:flex;flex-direction:column;line-height:1}
  .brand .big{font-size:10.5px;letter-spacing:.4px}
  .brand .small{font-size:3.6px;letter-spacing:1.4px;margin-top:1px}

  /* grey panel + numbered list */
  .panel{position:absolute;top:37px;right:0;bottom:0;background:var(--panel-grey)}
  .list{position:absolute;list-style:none}
  .list li{height:30px;display:flex;align-items:center;gap:13px;font-size:6.6px;font-weight:600;color:var(--blue)}
  .list .dot{width:26px;height:26px;border-radius:50%;background:var(--blue);color:var(--white);font-size:10px;font-weight:700;display:flex;align-items:center;justify-content:center;flex:none}
  .list li:first-child{margin-top:0}
  .heading{position:absolute;left:25px;color:var(--blue);font-weight:700;font-size:13px;line-height:1.2}
  .heading .soft{color:var(--title-grey);font-weight:600}
  .page{position:absolute;right:8px;bottom:8px;width:20px;height:20px;border-radius:50%;background:var(--blue);color:var(--white);font-size:9px;font-weight:700;display:flex;align-items:center;justify-content:center}

  .photo{position:absolute}
  .blue-box{position:absolute;background:var(--blue);color:var(--white);font-weight:700;font-size:13px;line-height:1.2}

  /* cover */
  .cover .wash{position:absolute;top:0;right:0;width:210px;height:100%;background:linear-gradient(90deg,rgba(127,140,204,0) 0%,#a7b0dc 35%,#7d8acb 100%)}
  .cover .art{position:absolute;left:155px;top:8px;width:180px;height:180px;border-radius:6px;background:radial-gradient(circle at 40% 45%,#b4b7c9 0%,rgba(140,150,205,.55) 45%,rgba(125,138,203,0) 75%)}
  .cover h1{position:absolute;left:24px;top:32px;font-size:29px;font-weight:700;line-height:1.16;color:var(--blue)}
  .cover h1 span{display:block;color:var(--title-grey)}
  .cover .brand{top:150px;left:25px;gap:12px}
  .cover .brand .mark{width:20px;height:20px;border-width:2.2px}
  .cover .brand .big{font-size:14px}
  .cover .brand .small{font-size:5px;letter-spacing:2px}

  .quote{position:absolute;left:17px;top:45px;width:115px;font-size:13.5px;font-weight:700;line-height:1.16;color:var(--blue)}
  .quote .soft{color:var(--title-grey)}
  .fine{position:absolute;left:17px;top:140px;width:105px;font-size:4.6px;line-height:1.55;color:#222}

  .bullets{position:absolute;left:24px;top:105px;list-style:none}
  .bullets li{font-size:6.6px;font-weight:600;color:var(--blue);height:14.2px;display:flex;align-items:center}
  .bullets li::before{content:"";width:2px;height:2px;border-radius:50%;background:var(--blue);margin-right:10px}

  .thanks{background:var(--blue);display:flex;align-items:center;justify-content:center}
  .thanks h2{color:var(--white);font-size:32px;font-weight:700}
</style>
</head>
<body>

<!-- 1 cover -->
<section class="slide col1 row1 cover">
  <div class="wash"></div>
  <div class="art" role="img" aria-label="Illustration of a megaphone with a stream of media icons: TV, radio, newspaper, satellite and phones"></div>
  <h1>Media<span>Training</span></h1>
  <div class="brand"><div class="mark"></div><div class="words"><span class="big">HARLOW</span><span class="small">COMMUNICATIONS</span></div></div>
</section>

<!-- 2 -->
<section class="slide col2 row1">
  <div class="section-band"><span class="num">Section 1:</span><span class="name">Introduction to Media Training</span></div>
  <div class="brand"><div class="mark"></div><div class="words"><span class="big">HARLOW</span><span class="small">COMMUNICATIONS</span></div></div>
  <div class="panel" style="left:165px"></div>
  <p class="heading" style="top:84px"><span class="soft">What is</span><br>media training?</p>
  <ul class="list" style="left:152px;top:62px">
    <li><span class="dot">01</span>It’s not natural</li>
    <li><span class="dot">02</span>It requires practice</li>
    <li><span class="dot">03</span>It’s about developing a mindset</li>
  </ul>
  <span class="page">2</span>
</section>

<!-- 3 -->
<section class="slide col3 row1">
  <div class="section-band"><span class="num">Section 1:</span><span class="name">Introduction to Media Training</span></div>
  <div class="brand"><div class="mark"></div><div class="words"><span class="big">HARLOW</span><span class="small">COMMUNICATIONS</span></div></div>
  <p class="quote">Training <span class="soft">and</span> preparation <span class="soft">are the difference between</span> success <span class="soft">and</span> failure.</p>
  <p class="fine">Sample body copy sits here, a short note on why steady practice and clear preparation shape every interview. Replace with client text.</p>
  <div class="photo" role="img" aria-label="Still photo of a man in a suit during a televised interview" style="left:126px;top:44px;width:208px;height:117px;background:linear-gradient(135deg,#5d6660,#3c413d 60%,#2b2f2c)"></div>
  <span class="page">3</span>
</section>

<!-- 4 -->
<section class="slide col1 row2">
  <div class="section-band"><span class="num">Section 2:</span><span class="name">Preparation</span></div>
  <div class="brand"><div class="mark"></div><div class="words"><span class="big">HARLOW</span><span class="small">COMMUNICATIONS</span></div></div>
  <div class="panel" style="left:130px"></div>
  <p class="heading" style="top:106px">Goals:</p>
  <ul class="list" style="left:116px;top:52px">
    <li><span class="dot">01</span>Learn how to prepare</li>
    <li><span class="dot">02</span>Develop a strategy</li>
    <li><span class="dot">03</span>Clarify message</li>
    <li><span class="dot">03</span>Build a practice approach</li>
  </ul>
  <span class="page">4</span>
</section>

<!-- 5 -->
<section class="slide col2 row2">
  <div class="section-band"><span class="num">Section 2:</span><span class="name">Preparation</span></div>
  <div class="brand"><div class="mark"></div><div class="words"><span class="big">HARLOW</span><span class="small">COMMUNICATIONS</span></div></div>
  <div class="blue-box" style="left:0;top:46px;width:146px;height:51px;padding:9px 0 0 23px">What to<br>negotiate?</div>
  <div class="photo" role="img" aria-label="Photo of a woman shaking hands with a man across a camera on a tripod in a bright office" style="left:146px;top:46px;width:186px;height:124px;background:linear-gradient(120deg,#dfe4ea,#b9c3cf 50%,#5c6a80)"></div>
  <ul class="bullets">
    <li>Timing and location</li>
    <li>Rules of recording/broadcast</li>
    <li>Rules of translation</li>
    <li>Questions</li>
    <li>Recording (for accuracy)</li>
  </ul>
  <span class="page">5</span>
</section>

<!-- 6 -->
<section class="slide col3 row2">
  <div class="section-band"><span class="num">Section 2:</span><span class="name">Preparation</span></div>
  <div class="brand"><div class="mark"></div><div class="words"><span class="big">HARLOW</span><span class="small">COMMUNICATIONS</span></div></div>
  <div class="blue-box" style="left:21px;top:46px;width:223px;height:151px;padding:12px 0 0 11px">Create<br>your<br>story</div>
  <div class="photo" role="img" aria-label="Broadcast still of officials greeting a line of schoolchildren in red and white uniforms" style="left:90px;top:46px;width:243px;height:133px;background:linear-gradient(160deg,#c9c4c0,#b04a4e 55%,#6e5f63)"></div>
  <span class="page">6</span>
</section>

<!-- 7 -->
<section class="slide col1 row3">
  <div class="section-band"><span class="num">Section 2:</span><span class="name">Preparation</span></div>
  <div class="brand"><div class="mark"></div><div class="words"><span class="big">HARLOW</span><span class="small">COMMUNICATIONS</span></div></div>
  <div class="panel" style="left:165px"></div>
  <p class="heading" style="top:101px">On the record:</p>
  <ul class="list" style="left:152px;top:61px">
    <li><span class="dot">01</span>Everything for print</li>
    <li><span class="dot">02</span>Your name for attribution</li>
    <li><span class="dot">03</span>Always assume everything is on the record</li>
  </ul>
  <span class="page">7</span>
</section>

<!-- 8 -->
<section class="slide col2 row3">
  <div class="section-band"><span class="num">Section 2:</span><span class="name">Preparation</span></div>
  <div class="brand"><div class="mark"></div><div class="words"><span class="big">HARLOW</span><span class="small">COMMUNICATIONS</span></div></div>
  <div class="panel" style="left:165px"></div>
  <p class="heading" style="top:97px">Off the record:</p>
  <ul class="list" style="left:152px;top:61px">
    <li><span class="dot">01</span>Not for print</li>
    <li><span class="dot">02</span>Not for attribution</li>
    <li><span class="dot">03</span>Doesn’t mean it won’t be used/printed</li>
  </ul>
  <span class="page">8</span>
</section>

<!-- 9 -->
<section class="slide col3 row3">
  <div class="section-band"><span class="num">Section 2:</span><span class="name">Preparation</span></div>
  <div class="brand"><div class="mark"></div><div class="words"><span class="big">HARLOW</span><span class="small">COMMUNICATIONS</span></div></div>
  <div class="panel" style="left:178px"></div>
  <p class="heading" style="left:24px;top:100px">On Background:</p>
  <ul class="list" style="left:165px;top:55px">
    <li><span class="dot">01</span>Education</li>
    <li><span class="dot">02</span>Context for print</li>
    <li><span class="dot">03</span>Can be used with attribution</li>
    <li><span class="dot">03</span>Attribution to be negotiated</li>
  </ul>
  <span class="page">9</span>
</section>

<!-- 10 -->
<section class="slide col1 row4">
  <div class="section-band"><span class="num">Section 2:</span><span class="name">Preparation</span></div>
  <div class="brand"><div class="mark"></div><div class="words"><span class="big">HARLOW</span><span class="small">COMMUNICATIONS</span></div></div>
  <div class="blue-box" style="left:0;top:43px;width:107px;height:51px;padding:8px 0 0 24px">Preparation<br>Matters!</div>
  <div class="photo" role="img" aria-label="Video still of two people seated at a round table on a dark red talk-show set" style="left:107px;top:43px;width:225px;height:122px;background:radial-gradient(ellipse at 50% 45%,#8a2a22,#4a1411 55%,#0d0d0d 90%)"></div>
  <span class="page">10</span>
</section>

<!-- 11 -->
<section class="slide col2 row4">
  <div class="section-band"><span class="num">Section 2:</span><span class="name">Preparation</span></div>
  <div class="brand"><div class="mark"></div><div class="words"><span class="big">HARLOW</span><span class="small">COMMUNICATIONS</span></div></div>
  <div class="panel" style="left:178px"></div>
  <p class="heading" style="top:101px">Schedule</p>
  <ul class="list" style="left:165px;top:53px">
    <li><span class="dot">01</span>Develop Q/A</li>
    <li><span class="dot">02</span>Write answers but also vocalize</li>
    <li><span class="dot">03</span>Practice: table</li>
    <li><span class="dot">03</span>Practice: mock</li>
  </ul>
  <span class="page">11</span>
</section>

<!-- 12 -->
<section class="slide col3 row4 thanks">
  <h2>Thank You</h2>
</section>

</body>
</html>
```